Maple Crest Branding for Contracts and Customer facing documents

We are hoping to create a themed branding for our company. We would like to leverage this across our contracts, documents, and all client information and proposals. www.HomesByMapleCrest.example is our website. We are selling high end custom homes. We am intending to use this template for a Lead Magnet and other marketing.

Target Market(s)

Luxury Custom Home Buyers

Industry/Entity Type

Residential Construction

Other font styles liked:
• You may choose, We want to be elegant but very legible and professional

Colors
0054AA
0677BA
7BADD7
CADEEF
E8F1F8

```html
<!DOCTYPE html>
<html lang="en">
<head>
<meta charset="utf-8">
<title>Maple Crest – New Client Pre-Contract Package</title>
<link rel="stylesheet" href="https://fonts.googleapis.com/css2?family=Cinzel:wght@400;600&family=Montserrat:wght@400;600&display=swap">
<style>
  :root{
    --bg:#e6e6e6;
    --navy:#022a52;
    --navy-deep:#061a33;
    --gold:#c9a15a;
    --ink:#1b2f4e;
    --paper:#ffffff;
    --rule:#2a3f5f;
  }
  *{box-sizing:border-box;margin:0;padding:0}
  html,body{width:1200px;height:1200px;overflow:hidden;background:var(--bg)}
  body{position:relative;font-family:"Montserrat",sans-serif;color:var(--ink)}
  .page{position:absolute;width:359px;height:465px;background:var(--paper);overflow:hidden}
  .p1{left:51px;top:132px}
  .p2{left:424px;top:132px}
  .p3{left:797px;top:132px}
  .p4{left:51px;top:611px}
  .p5{left:424px;top:611px}
  .p6{left:797px;top:611px;background:var(--navy)}
  .abs{position:absolute}
  .caps{font-family:"Cinzel",serif;text-transform:uppercase;letter-spacing:.12em}
  .footer-band{position:absolute;left:0;right:0;bottom:0;height:21px;background:var(--navy)}

  /* cover */
  .cover-bg{position:absolute;inset:0;background:linear-gradient(160deg,#0c2c55 0%,#0a2447 45%,#061a33 100%)}
  .cover-center{position:absolute;left:0;right:0;text-align:center;color:var(--gold)}
  .brand-mark{display:inline-block;width:10px;height:10px;border-radius:50%;background:currentColor;margin-bottom:6px}
  .brand-name{font-family:"Cinzel",serif;font-weight:600;letter-spacing:.04em}
  .cover .brand-name{font-size:26px}
  .cover .sub{font-size:8px;letter-spacing:.14em}
  .cover .addr{font-size:5.2px;letter-spacing:.16em}
  .package-title{font-size:8px;letter-spacing:.14em}
  .package-item{font-size:6.2px;letter-spacing:.16em}
  .dot{font-size:6px}
  .cover-contact{font-size:5.4px;letter-spacing:.16em;line-height:8.5px}

  /* headers */
  .letterhead{left:18px;top:16px;display:flex;align-items:flex-start;gap:8px;color:var(--navy)}
  .letterhead .square{width:12px;height:12px;background:var(--navy);margin-top:10px}
  .letterhead .brand-name{font-size:22px;line-height:26px}
  .letterhead .sub{font-size:6.6px;letter-spacing:.14em;margin-top:2px}
  .letterhead .contact{font-size:3.6px;letter-spacing:.1em;margin-top:3px}

  .step{font-family:"Cinzel",serif;font-weight:600;font-size:10px;letter-spacing:.16em;color:var(--navy)}
  .step::before{content:"•";margin-right:6px;font-size:9px}
  .body-text{font-size:6.9px;line-height:10.6px;color:var(--ink)}
  .body-text p{margin-bottom:5.8px}
  .body-text ul{list-style:none}
  .body-text li{margin-bottom:5.8px;padding-left:4px;text-indent:-4px}
  .body-text li::before{content:"· "}
  .bold-list li{margin-bottom:0;font-weight:600}
  .fee{font-weight:600}

  .section-bar{left:72px;right:0;top:49px;height:20px;background:var(--navy);color:#fff;
    font-family:"Cinzel",serif;font-weight:600;font-size:11.5px;letter-spacing:.14em;padding:3px 0 0 4px;text-transform:uppercase}

  .signatures{font-size:5.4px;color:var(--ink)}
  .sig-row{position:absolute;display:flex;align-items:flex-end;width:100%}
  .sig-label{width:68px}
  .sig-line{width:110px;border-bottom:.6px solid var(--rule);height:6px;margin-right:4px}
  .date-label{margin-right:2px}
  .date-line{width:50px;border-bottom:.6px solid var(--rule);height:6px}

  .photo{position:absolute}
  .photo-meeting{left:0;right:0;top:284px;height:160px;
    background:linear-gradient(180deg,rgba(255,255,255,1) 0%,#d9d3c8 25%,#9a8a73 60%,#5b4a38 100%)}
  .photo-field{left:0;right:0;top:330px;height:114px;
    background:linear-gradient(180deg,#fff 0%,#dfe3e6 30%,#8fa06a 65%,#6f8c3a 100%)}
  .photo-dig{left:0;top:148px;width:114px;height:95px;
    background:linear-gradient(180deg,#cfe1ef 0%,#7f9d5a 45%,#a07a4e 100%)}
  .photo-plans{left:0;top:198px;width:114px;height:75px;
    background:linear-gradient(90deg,#ffffff 0%,#e6e2da 35%,#cfc7b8 100%)}

  .back-center{position:absolute;left:0;right:0;text-align:center;color:#fff}
  .p6 .brand-name{font-size:24px}
  .p6 .sub{font-size:7.5px;letter-spacing:.14em}
  .p6 .small{font-size:4.2px;letter-spacing:.12em}
</style>
</head>
<body>

<!-- Cover -->
<section class="page p1 cover">
  <div class="cover-bg" role="img" aria-label="Dark navy photograph of modern architecture"></div>
  <div class="cover-center" style="top:84px">
    <span class="brand-mark"></span>
    <div class="brand-name">Maple Crest</div>
  </div>
  <div class="cover-center caps sub" style="top:134px">Custom Homes</div>
  <div class="cover-center caps addr" style="top:148px">218 Ridgeview Ln., #4 Fairhaven VA, 20000</div>
  <div class="cover-center caps package-title" style="top:219px">New Client Pre-Contract Package</div>
  <div class="cover-center dot" style="top:233px">•</div>
  <div class="cover-center caps package-item" style="top:244px">Initial Consultation</div>
  <div class="cover-center dot" style="top:256px">•</div>
  <div class="cover-center caps package-item" style="top:267px">Site Meeting</div>
  <div class="cover-center dot" style="top:279px">•</div>
  <div class="cover-center caps package-item" style="top:290px">Drainfield Exploration</div>
  <div class="cover-center dot" style="top:302px">•</div>
  <div class="cover-center caps package-item" style="top:313px">Design Process</div>
  <div class="cover-center caps cover-contact" style="top:429px">
    By: Evan Hartley<br>Phone: 555-017-3391<br>www.HomesByMapleCrest.example
  </div>
</section>

<!-- Step One -->
<section class="page p2">
  <div class="abs letterhead">
    <div class="square"></div>
    <div>
      <div class="brand-name">Maple Crest</div>
      <div class="caps sub">Custom Homes</div>
      <div class="caps contact">www.HomesByMapleCrest.example · 218 Ridgeview Ln · #4 Fairhaven VA, 20000 · (555) 014-2280</div>
    </div>
  </div>
  <div class="abs step" style="left:74px;top:108px">Step One</div>
  <div class="abs body-text" style="left:74px;top:129px;width:225px">
    <p>The first step in the process is an initial office consultation.</p>
    <p>The goals for this meeting is to accomplish the following:</p>
    <ul>
      <li>Opportunity to meet in person to establish rapport and the start of building a long relationship.</li>
      <li>We will review our team, building process and timelines, and why we are passionate about what we do.</li>
      <li>Discuss your overall plans and desires and identify a budget.</li>
      <li>Discuss our preferred lenders who specialize in construction to permanent loans.</li>
      <li>Establish a next step.</li>
    </ul>
  </div>
  <div class="photo photo-meeting" role="img" aria-label="Photograph of a team meeting around an office table"></div>
  <div class="footer-band"></div>
</section>

<!-- Step Two -->
<section class="page p3">
  <div class="abs step" style="left:74px;top:60px">Step Two</div>
  <div class="abs body-text" style="left:74px;top:80px;width:250px">
    <p>The second critical step in the process is a site meeting on your property. The property has a large impact on your overall house design. At this meeting we can locate the ideal house placement based on the topography of the land to obtain the best siting on the property to capture views and obtain the desired grading and a potential walk-out basement scenario. In addition, we can identify any necessary clearing required, length of driveway needed and discuss any potential obstacles that could affect the design or build. The fee for this service is $300.00 for a site meeting scheduled during the weekday. If you move forward with a construction contract, then we will credit this amount towards your new home.</p>
    <p style="margin-bottom:0"><span class="fee">Site Meeting Fee: $300.00</span><br>By signing below and paying the appropriate fee, you agree to the terms and authorize Maple Crest to proceed with the following services.</p>
  </div>
  <div class="abs signatures" style="left:74px;top:252px;width:260px">
    <div class="sig-row" style="top:0"><span class="sig-label">Customer Signature(s):</span><span class="sig-line"></span><span class="date-label">Date:</span><span class="date-line"></span></div>
    <div class="sig-row" style="top:21px"><span class="sig-label"></span><span class="sig-line"></span><span class="date-label">Date:</span><span class="date-line"></span></div>
    <div class="sig-row" style="top:42px"><span class="sig-label">Maple Crest, LLC.</span><span class="sig-line"></span><span class="date-label">Date:</span><span class="date-line"></span></div>
  </div>
  <div class="photo photo-field" role="img" aria-label="Photograph of green rolling farmland under a hazy sky"></div>
  <div class="footer-band"></div>
</section>

<!-- Step Three -->
<section class="page p4">
  <div class="abs section-bar">Drainfield Exploration</div>
  <div class="abs step" style="left:74px;top:77px">Step Three</div>
  <div class="abs body-text" style="left:74px;top:97px;width:250px">
    <p>The third critical step in the process will give Maple Crest the approval to identify issues and any additional up front costs so we can plan accordingly and project an accurate budget number. The fee of $4,500.00 will include the following:</p>
  </div>
  <div class="photo photo-dig" role="img" aria-label="Photograph of an excavator clearing a wooded lot"></div>
  <div class="abs body-text" style="left:122px;top:144px;width:205px">
    <ul class="bold-list" style="margin-bottom:6px">
      <li>Backhoe/Excavation Service</li>
      <li>Soil Evaluation</li>
      <li>Preliminary Surveying</li>
      <li>Drainfield Design</li>
    </ul>
    <p>Please note, that some of these services will not be necessary prior to contract and are based on the location of your homesite and individual county guidelines. This fee paid up front is typically included in your overall budget number and will be adjusted on the final budget.</p>
  </div>
  <div class="abs body-text" style="left:74px;top:255px;width:252px">
    <p><span class="fee">Drainfield Exploration Fee: $4,500.00</span><br>By Signing below and paying the appropriate fees, you agree to the terms and authorize Maple Crest to proceed with the following services on your new home. In addition, you understand that no work will commence until all signatures are completed and payment is received in full.</p>
  </div>
  <div class="abs signatures" style="left:74px;top:326px;width:260px">
    <div class="sig-row" style="top:0"><span class="sig-label">Customer Signature(s):</span><span class="sig-line"></span><span class="date-label">Date:</span><span class="date-line"></span></div>
    <div class="sig-row" style="top:21px"><span class="sig-label"></span><span class="sig-line"></span><span class="date-label">Date:</span><span class="date-line"></span></div>
    <div class="sig-row" style="top:42px"><span class="sig-label">Maple Crest, LLC.</span><span class="sig-line"></span><span class="date-label">Date:</span><span class="date-line"></span></div>
  </div>
  <div class="footer-band"></div>
</section>

<!-- Step Four -->
<section class="page p5">
  <div class="abs section-bar">Design Fee</div>
  <div class="abs step" style="left:74px;top:77px">Step Four</div>
  <div class="abs body-text" style="left:74px;top:97px;width:252px">
    <p>It is our goal to help you reach a point where you may begin construction on your new custom home containing all of your wishes and desires. This step in the process will engage Maple Crest to create a concept and then a set of construction drawings in order to accurately price and establish a budget for your new custom home. You will be allowed one revision after the construction drawings are completed. Additional revisions and drawing time will be at an additional charge. We will advise you before we enter into additional drawing time requirements.</p>
  </div>
  <div class="photo photo-plans" role="img" aria-label="Photograph of architectural plans rolled out on a desk"></div>
  <div class="abs body-text" style="left:122px;top:192px;width:205px">
    <p>Drawing fees will be set at $85.00 per hour. The fee to provide this service to our clients is $10,000.00 which also includes a detailed electrical plan. All of our designs are created in house, which will save you thousands of dollars in outside architectural fees. In addition, we will work with you closely to personally design your dream home. This fee is non-refundable and separate from any contract deposit required at the time of construction contract.</p>
  </div>
  <div class="abs body-text" style="left:74px;top:285px;width:254px">
    <p><span class="fee">Custom Home Plan Creation and Detailed Electrical Plan: $10,000.00</span><br>By Signing below and paying the appropriate fees, you agree to the terms and authorize Maple Crest to proceed with the construction drawings on your new home. In addition, you understand that no work will commence until all signatures are completed and payment is received in full.</p>
  </div>
  <div class="abs signatures" style="left:74px;top:361px;width:260px">
    <div class="sig-row" style="top:0"><span class="sig-label">Customer Signature(s):</span><span class="sig-line"></span><span class="date-label">Date:</span><span class="date-line"></span></div>
    <div class="sig-row" style="top:21px"><span class="sig-label"></span><span class="sig-line"></span><span class="date-label">Date:</span><span class="date-line"></span></div>
    <div class="sig-row" style="top:42px"><span class="sig-label">Maple Crest, LLC.</span><span class="sig-line"></span><span class="date-label">Date:</span><span class="date-line"></span></div>
  </div>
  <div class="footer-band"></div>
</section>

<!-- Back cover -->
<section class="page p6">
  <div class="back-center" style="top:366px">
    <span class="brand-mark"></span>
    <div class="brand-name">Maple Crest</div>
  </div>
  <div class="back-center caps sub" style="top:414px">Custom Homes</div>
  <div class="back-center caps small" style="top:425px">www.HomesByMapleCrest.example</div>
  <div class="back-center caps small" style="top:434px">218 Ridgeview Ln · #4 Fairhaven VA, 20000 · (555) 014-2280</div>
</section>

</body>
</html>
```